construction co.logo(ie.highway,heavy equip)

need a design for a new construction company in washington state,office is located on the water (beach front)also use a 1952 dunmore keel avalis as portable office,or the standard bold construction type logo's,these are just thoughts and not necassarily direction

Target Market(s)

I will be working as a sub to much larger general contractors and am looking for a strong,stable appearance.

Industry/Entity Type

Construction

```html
<!DOCTYPE html>
<html lang="en">
<head>
<meta charset="utf-8">
<title>North Sound General Contractors – Business Card</title>
<link rel="stylesheet" href="https://fonts.googleapis.com/css2?family=Jost:wght@800&family=Open+Sans:wght@300;400;700&display=swap">
<style>
  :root {
    --page: #ffffff;
    --card: #94b5e0;
    --brand: #1f3f99;
    --navy: #1f3f99;
    --ink: #111111;
    --body-ink: #1e1e1e;
  }
  html, body {
    margin: 0;
    padding: 0;
    width: 1200px;
    height: 1200px;
    overflow: hidden;
    background: var(--page);
  }
  .canvas {
    position: relative;
    width: 1200px;
    height: 1200px;
  }
  .card {
    position: absolute;
    left: 278px;
    top: 47px;
    width: 635px;
    height: 1107px;
    background: var(--card);
    overflow: hidden;
  }
  .brand {
    position: absolute;
    left: 30px;
    top: 28px;
    display: flex;
    align-items: center;
    gap: 14px;
  }
  .brand-dot {
    width: 104px;
    height: 104px;
    border-radius: 50%;
    background: var(--brand);
    flex: none;
  }
  .brand-name {
    margin: 0;
    font-family: "Open Sans", sans-serif;
    font-weight: 700;
    color: var(--brand);
    line-height: 1;
    white-space: nowrap;
  }
  .brand-name .line-main {
    display: block;
    font-size: 60px;
    letter-spacing: -1.5px;
  }
  .brand-name .line-sub {
    display: block;
    font-size: 36px;
    margin-top: 2px;
    letter-spacing: -0.5px;
  }
  .person {
    position: absolute;
    left: 0;
    right: 0;
    top: 428px;
    text-align: center;
  }
  .person-name {
    margin: 0;
    font-family: "Jost", sans-serif;
    font-weight: 800;
    font-size: 80px;
    line-height: 1;
    color: var(--ink);
    letter-spacing: -1px;
    white-space: nowrap;
  }
  .person-role {
    margin: -4px 0 0;
    font-family: "Open Sans", sans-serif;
    font-weight: 300;
    font-size: 60px;
    line-height: 1;
    color: var(--ink);
  }
  .contact {
    position: absolute;
    left: 0;
    right: 0;
    top: 722px;
    margin: 0;
    text-align: center;
    font-family: "Open Sans", sans-serif;
    font-weight: 400;
    font-size: 30px;
    line-height: 40px;
    color: var(--body-ink);
    font-style: normal;
  }
  .contact span { display: block; white-space: nowrap; }
  .wave-band {
    position: absolute;
    left: 0;
    right: 0;
    bottom: 0;
    height: 140px;
    background: linear-gradient(to bottom, var(--card) 0%, var(--navy) 100%);
  }
</style>
</head>
<body>
<div class="canvas">
  <section class="card">
    <header class="brand">
      <div class="brand-dot"></div>
      <h1 class="brand-name">
        <span class="line-main">NORTH SOUND</span>
        <span class="line-sub">GENERAL CONTRACTORS</span>
      </h1>
    </header>

    <div class="person">
      <h2 class="person-name">DALE HARMON</h2>
      <p class="person-role">owner</p>
    </div>

    <address class="contact">
      <span>48 tidewater lane marrow bay, wa 98277</span>
      <span>360-555-0142</span>
      <span>northsoundbuilders@harborpost.net</span>
    </address>

    <div class="wave-band" role="img" aria-label="Decorative sweeping wave band in navy, white and light blue"></div>
  </section>
</div>
</body>
</html>
```